New Business Card Design Project

I need a meaningful new business card. Therefore, the website should convey growth, joy, uniqueness, workout and a bit of luxury.
Color scheme should be petrol, gold and matching colors.

```html
<!DOCTYPE html>
<html lang="de">
<head>
<meta charset="utf-8">
<title>Corewell Studio – Visitenkarte</title>
<link href="https://fonts.googleapis.com/css2?family=Open+Sans:wght@400;700&display=swap" rel="stylesheet">
<style>
  :root {
    --stage: #333335;
    --card-dark: #212125;
    --petrol: #17ad9f;
    --petrol-deep: #0f8a7f;
    --text-light: #f2f2f2;
    --text-muted: #5f6166;
  }
  * { box-sizing: border-box; margin: 0; padding: 0; }
  html, body {
    width: 1200px; height: 780px; overflow: hidden;
    background: var(--stage);
    font-family: "Open Sans", Arial, sans-serif;
  }
  .sheet {
    position: relative; width: 1200px; height: 780px;
    display: flex; align-items: center; justify-content: center; gap: 40px;
  }
  .card {
    position: relative; width: 540px; height: 320px; overflow: hidden;
  }
  .card--front { background: var(--card-dark); }
  .card--back { background: var(--petrol); display: flex; align-items: center; justify-content: center; }

  .brand {
    position: absolute; left: 36px; top: 110px;
    display: flex; align-items: center; gap: 12px;
  }
  .brand__dot {
    width: 18px; height: 18px; border-radius: 50%; background: var(--petrol);
  }
  .brand__name {
    font-weight: 700; font-size: 28px; color: var(--petrol); letter-spacing: 0.5px;
  }

  .accent-bar {
    position: absolute; top: 0; right: 0; width: 10px; height: 64px; background: var(--petrol);
  }
  .identity {
    position: absolute; right: 34px; top: 30px; text-align: right;
  }
  .identity__name {
    font-weight: 700; font-size: 30px; color: var(--petrol); line-height: 1.1;
  }
  .identity__role {
    font-size: 14px; color: var(--text-muted); margin-top: 2px;
  }

  .contacts {
    position: absolute; right: 30px; bottom: 36px; list-style: none;
  }
  .contacts li {
    display: flex; justify-content: flex-end; align-items: center; gap: 10px;
    font-size: 15px; color: var(--text-light); line-height: 26px;
  }
  .contacts svg { width: 14px; height: 14px; flex: none; }

  .back-brand {
    display: flex; align-items: center; gap: 14px;
  }
  .back-brand__dot {
    width: 24px; height: 24px; border-radius: 50%; background: var(--petrol-deep);
  }
  .back-brand__name {
    font-weight: 700; font-size: 38px; color: var(--petrol-deep);
  }
</style>
</head>
<body>
<main class="sheet">
  <section class="card card--front" aria-label="Visitenkarte Vorderseite">
    <div class="brand">
      <span class="brand__dot"></span>
      <span class="brand__name">Corewell Studio</span>
    </div>

    <div class="accent-bar"></div>
    <div class="identity">
      <p class="identity__name">Lena Marwitz</p>
      <p class="identity__role">Pilates Studio Trainerin</p>
    </div>

    <ul class="contacts">
      <li>+49 170 5550147
        <svg viewBox="0 0 16 16" aria-hidden="true"><path fill="#17ad9f" d="M3.6 1.5l2.3 2.6-1.2 1.7c.9 2 2.4 3.5 4.4 4.4l1.7-1.2 2.6 2.3-1.3 2.2C6.5 13.2 2.8 9.5 1.5 3z"/></svg>
      </li>
      <li>corewell_studio
        <svg viewBox="0 0 16 16" aria-hidden="true"><circle cx="8" cy="8" r="7" fill="#17ad9f"/></svg>
      </li>
      <li>hello@corewell-studio.de
        <svg viewBox="0 0 16 16" aria-hidden="true"><rect x="1" y="3" width="14" height="10" rx="1.5" fill="#17ad9f"/><path d="M1.5 4l6.5 5 6.5-5" fill="none" stroke="#212125" stroke-width="1.4"/></svg>
      </li>
      <li>www.corewell-studio.de
        <svg viewBox="0 0 16 16" aria-hidden="true"><circle cx="8" cy="8" r="7" fill="#17ad9f"/></svg>
      </li>
    </ul>
  </section>

  <section class="card card--back" aria-label="Visitenkarte Rückseite">
    <div class="back-brand">
      <span class="back-brand__dot"></span>
      <span class="back-brand__name">Corewell Studio</span>
    </div>
  </section>
</main>
</body>
</html>
```